Bright Harbor Renovations
Business Card  - Construction
Business Card
Professional
Derek Molloy - Owner
7182 Tamsworth Rd. Modesto, Ca 95471 209-647-2913
brightharborrenovations@mailbox-example.com
brightharborrenovations-example.com
Marcmithamo Marcmithamo

```html
<!DOCTYPE html>
<html lang="en">
<head>
<meta charset="utf-8">
<title>Bright Harbor Renovations – Business Card</title>
<link href="https://fonts.googleapis.com/css2?family=Open+Sans:wght@400;600;700&display=swap" rel="stylesheet">
<style>
  :root {
    --stage: #232323;
    --blue-deep: #0d4f9a;
    --blue-mid: #1570bf;
    --blue-bright: #1aa3d6;
    --card-white: #ffffff;
    --ink-grey: #6d6f72;
    --rule-grey: #d3d5d8;
    --name-blue: #1a5ea8;
  }
  * { box-sizing: border-box; margin: 0; padding: 0; }
  html, body { width: 1200px; height: 750px; overflow: hidden; }
  body {
    background: var(--stage);
    font-family: "Open Sans", Arial, sans-serif;
    position: relative;
  }
  .card {
    position: absolute;
    width: 520px;
    height: 298px;
    border-radius: 16px;
    overflow: hidden;
  }

  /* Front */
  .card-front {
    left: 60px; top: 110px;
    background: radial-gradient(circle at 62% 45%, var(--blue-bright) 0%, var(--blue-mid) 40%, var(--blue-deep) 100%);
    color: #fff;
  }
  .front-brand {
    position: absolute; right: 30px; top: 28px;
    text-align: right;
  }
  .front-name {
    font-weight: 700; font-size: 19px; letter-spacing: 1.5px;
    text-transform: uppercase; line-height: 1.25;
  }
  .services {
    list-style: none; margin-top: 10px;
    font-size: 12px; line-height: 1.45;
  }
  .services li::after {
    content: ""; display: inline-block;
    width: 4px; height: 4px; border-radius: 50%;
    background: #fff; margin-left: 10px; vertical-align: middle;
  }

  /* Back */
  .card-back {
    left: 620px; top: 342px;
    background: var(--card-white);
  }
  .back-brand {
    position: absolute; left: 24px; top: 116px; width: 190px;
    display: flex; align-items: center; gap: 10px;
  }
  .brand-square { width: 14px; height: 14px; background: var(--blue-mid); flex: none; }
  .back-name {
    color: var(--blue-mid); font-weight: 700; font-size: 14px;
    letter-spacing: 0.8px; text-transform: uppercase; line-height: 1.25;
  }
  .divider {
    position: absolute; left: 224px; top: 36px;
    width: 1px; height: 130px; background: var(--rule-grey);
  }
  .contact {
    position: absolute; left: 240px; top: 26px;
    color: var(--ink-grey); font-size: 12px; line-height: 1.45;
  }
  .person { color: var(--name-blue); font-weight: 700; font-size: 17px; line-height: 1.2; }
  .role { font-size: 12px; margin-bottom: 5px; }
  .address { margin-bottom: 5px; }
  .line { display: flex; align-items: center; gap: 7px; }
  .line svg { flex: none; }
  .line-email { font-size: 10.5px; }
  .swoosh { position: absolute; left: 0; top: 0; }
  .website {
    position: absolute; right: 20px; bottom: 34px;
    color: #fff; font-size: 11px; transform: rotate(-10deg);
    transform-origin: right bottom;
  }
</style>
</head>
<body>

<section class="card card-front" aria-label="Card front">
  <div class="front-brand">
    <p class="front-name">Bright Harbor<br>Renovations</p>
    <ul class="services">
      <li>Fire - Flood</li>
      <li>New Construction</li>
      <li>Kitchens &amp; Bath</li>
      <li>Termite/Dry Rot Repair</li>
    </ul>
  </div>
</section>

<section class="card card-back" aria-label="Card back">
  <svg class="swoosh" width="520" height="298" viewBox="0 0 520 298" aria-hidden="true">
    <defs>
      <linearGradient id="bandBlue" x1="0" y1="1" x2="1" y2="0">
        <stop offset="0" stop-color="#0d4f9a"/>
        <stop offset="0.55" stop-color="#1570bf"/>
        <stop offset="1" stop-color="#1aa3d6"/>
      </linearGradient>
      <linearGradient id="bandSilver" x1="0" y1="0" x2="1" y2="0">
        <stop offset="0" stop-color="#e4e6e8"/>
        <stop offset="0.5" stop-color="#9ea2a6"/>
        <stop offset="1" stop-color="#d8dadd"/>
      </linearGradient>
    </defs>
    <path d="M0 264 C150 256 260 248 340 224 C420 200 470 194 520 192 L520 298 L0 298 Z" fill="url(#bandSilver)"/>
    <path d="M0 274 C160 266 270 258 350 234 C430 212 475 206 520 205 L520 298 L0 298 Z" fill="url(#bandBlue)"/>
  </svg>

  <div class="back-brand">
    <span class="brand-square" aria-hidden="true"></span>
    <p class="back-name">Bright Harbor<br>Renovations</p>
  </div>

  <div class="divider" aria-hidden="true"></div>

  <div class="contact">
    <p class="person">Derek Molloy</p>
    <p class="role">Owner</p>
    <p class="address">7182 Tamsworth Rd.<br>Modesto, Ca 95471<br>License No., 1047762</p>
    <p class="line">
      <svg width="10" height="14" viewBox="0 0 10 14" aria-hidden="true"><rect x="1" y="0.5" width="8" height="13" rx="1.5" fill="none" stroke="#1570bf" stroke-width="1.3"/><circle cx="5" cy="11" r="0.9" fill="#1570bf"/></svg>
      209-647-2913
    </p>
    <p class="line line-email">
      <svg width="12" height="9" viewBox="0 0 12 9" aria-hidden="true"><rect width="12" height="9" rx="1" fill="#1570bf"/><path d="M0.5 0.8 L6 5 L11.5 0.8" fill="none" stroke="#fff" stroke-width="1"/></svg>
      brightharborrenovations@mailbox-example.com
    </p>
  </div>

  <p class="website">www.brightharborrenovations-example.com</p>
</section>

</body>
</html>
```